Door Company flyer for hardware sale

I need a flyer approximately 4" wide by 5" height. I need to promote one of the brands we carry (MARLOW) for a one day discount sale on Wednesday May 22, 2024. Our company name is TULVEN Commercial Door and our main vendor is Corvanta but we will have special pricing on MARLOW products which are the 3 pictures of hardware. I would like for the date to stand out in a different color. I want to use our logo colors which are gray, orange, and white but would like the date in a banner of a different color. We also want to add that we will have free tacos, prizes, and goodies.

Target Market(s)

Construction Industry

Industry/Entity Type

Construction

Colors
F0912C
F2A743
F7CA91
FBE8D2
FDF5EE
EE7325
F08F49
F5BC92
FAE3D3
FDF4ED

Requirements
Must have
• Pictures of hardware & logos I uploaded. Invite customers to join us for special pricing, free tacos, prizes and more.
Nice to have
• Promote the May 22 2024 event

```html
<!DOCTYPE html>
<html lang="en">
<head>
<meta charset="utf-8">
<title>TULVEN Commercial Door – One Day Discount Sale</title>
<link rel="stylesheet" href="https://fonts.googleapis.com/css2?family=Poppins:wght@400;500;600;700;800&family=Playfair+Display:wght@800&display=swap">
<style>
  :root {
    --orange: #ee7325;
    --orange-deep: #e2661b;
    --orange-bright: #f0912c;
    --gray-light: #d2d3d5;
    --gray-mid: #bcbdc0;
    --gray-text: #8a8b8e;
    --charcoal: #3b3c3e;
    --ink: #141414;
    --white: #ffffff;
    --page: #e4e4e4;
  }
  * { box-sizing: border-box; margin: 0; padding: 0; }
  html, body {
    width: 1003px; height: 1200px; overflow: hidden;
    background: var(--page);
    font-family: "Poppins", sans-serif;
  }
  .flyer {
    position: absolute; left: 29.5px; top: 10px;
    width: 944px; height: 1180px;
    background: var(--white);
    overflow: hidden;
  }
  .hero-backdrop {
    position: absolute; left: 0; top: 0; width: 944px; height: 700px;
    background: linear-gradient(100deg, var(--orange-deep) 0%, var(--orange) 45%, #e96d20 100%);
  }
  .headline-kicker {
    position: absolute; left: 166px; top: 62px;
    color: var(--white); font-weight: 600; font-size: 60px;
    line-height: 56px; letter-spacing: 2px;
  }
  .headline-sale { position: absolute; left: 0; top: 0; }
  .date-pill { position: absolute; left: 156px; top: 478px; width: 634px; height: 67px; }
  .date-day, .date-full {
    position: absolute; top: 0; height: 67px; line-height: 67px;
    font-size: 42px; letter-spacing: -1px;
  }
  .date-day { left: 30px; color: var(--ink); font-weight: 400; }
  .date-full { left: 314px; color: var(--white); font-weight: 700; }
  .product-card { position: absolute; top: 592px; width: 272px; height: 217px; }
  .product-photo {
    position: absolute; left: 24px; top: 24px; width: 224px; height: 150px; border-radius: 10px;
    background: radial-gradient(ellipse at center, #c9cacc 0%, #e6e7e8 60%, #ffffff 100%);
  }
  .join-title {
    position: absolute; left: 49px; width: 386px; top: 852px; text-align: center;
    color: var(--orange-bright); font-weight: 700; font-size: 58px; line-height: 62px; letter-spacing: -1px;
  }
  .pricing-banner { position: absolute; left: 49px; top: 917px; width: 386px; height: 40px; }
  .pricing-text {
    position: absolute; left: 0; width: 386px; top: 0; line-height: 40px; text-align: center;
    color: var(--white); font-weight: 600; font-size: 30px;
  }
  .perks {
    position: absolute; left: 40px; width: 404px; top: 963px; text-align: center;
    color: var(--ink); font-size: 28px; line-height: 34px; letter-spacing: -0.5px;
  }
  .brands-box {
    position: absolute; left: 513px; top: 865px; width: 387px; height: 125px;
    border: 1.5px solid var(--gray-mid);
  }
  .brands-label {
    position: absolute; left: 50%; top: -14px; transform: translateX(-50%);
    background: var(--white); padding: 0 8px; white-space: nowrap;
    color: var(--gray-text); font-weight: 600; font-size: 20px; line-height: 26px;
  }
  .brands-divider { position: absolute; left: 178px; top: 22px; width: 1.5px; height: 86px; background: var(--gray-light); }
  .brand-corvanta {
    position: absolute; left: 16px; top: 40px; width: 150px;
    display: flex; flex-direction: column; align-items: center; gap: 8px;
  }
  .brand-corvanta .brand-square { width: 30px; height: 30px; background: var(--orange); }
  .brand-corvanta .brand-name { color: var(--charcoal); font-weight: 700; font-size: 20px; letter-spacing: 1px; }
  .brand-marlow {
    position: absolute; left: 180px; width: 205px; top: 38px; text-align: center;
    color: var(--ink); font-weight: 800; font-size: 38px; letter-spacing: -1px; line-height: 44px;
  }
  .company-mark { position: absolute; left: 42px; top: 1050px; display: flex; align-items: center; gap: 16px; }
  .company-mark .mark-square { width: 54px; height: 54px; background: var(--orange-bright); }
  .company-name { color: var(--gray-text); font-weight: 700; }
  .company-name .line-1 { display: block; font-size: 58px; line-height: 54px; letter-spacing: 2px; }
  .company-name .line-2 { display: block; font-size: 17px; line-height: 22px; letter-spacing: 1.5px; }
  .contact-bands { position: absolute; left: 0; top: 0; }
  .contact-phone {
    position: absolute; left: 525px; top: 1063px; line-height: 43px;
    color: var(--white); font-size: 34px; letter-spacing: -0.3px;
  }
  .contact-phone strong { font-weight: 700; }
  .contact-web {
    position: absolute; left: 516px; top: 1106px; line-height: 30px;
    color: var(--ink); font-size: 22px;
  }
</style>
</head>
<body>
<main class="flyer">
  <div class="hero-backdrop" role="img" aria-label="Door hardware showroom photo washed in orange"></div>

  <h1 class="headline-kicker">ONE DAY<br>DISCOUNT</h1>

  <svg class="headline-sale" width="944" height="460" viewBox="0 0 944 460" aria-label="Sale">
    <text x="163" y="443" font-family="'Playfair Display', serif" font-weight="800" font-size="352"
          fill="#ffffff" textLength="626" lengthAdjust="spacingAndGlyphs">Sale</text>
  </svg>

  <div class="date-pill">
    <svg width="634" height="67" viewBox="0 0 634 67">
      <defs>
        <linearGradient id="dateDark" x1="0" y1="0" x2="1" y2="0">
          <stop offset="0" stop-color="#2b2c2e"/>
          <stop offset="0.6" stop-color="#5a5b5e"/>
          <stop offset="1" stop-color="#3a3b3d"/>
        </linearGradient>
      </defs>
      <path d="M33.5 0 H296 V67 H33.5 A33.5 33.5 0 0 1 33.5 0 Z" fill="#d2d3d5"/>
      <path d="M296 0 H600.5 A33.5 33.5 0 0 1 600.5 67 H296 Z" fill="url(#dateDark)"/>
    </svg>
    <span class="date-day">WEDNESDAY</span>
    <span class="date-full">MAY 22, 2024</span>
  </div>

  <div class="product-card" style="left:44px">
    <svg width="272" height="217" viewBox="0 0 272 217">
      <path d="M0 108 H272 V192 A25 25 0 0 1 247 217 H25 A25 25 0 0 1 0 192 Z" fill="#bcbdc0"/>
      <path d="M0 20 A20 20 0 0 1 20 0 H252 A20 20 0 0 1 272 20 V108 H0 Z" fill="#ffffff"/>
      <path d="M14 100 H258 V185 A20 20 0 0 1 238 205 H34 A20 20 0 0 1 14 185 Z" fill="#ffffff"/>
    </svg>
    <div class="product-photo" role="img" aria-label="Photo of a silver overhead door closer"></div>
  </div>
  <div class="product-card" style="left:336px">
    <svg width="272" height="217" viewBox="0 0 272 217">
      <path d="M0 108 H272 V192 A25 25 0 0 1 247 217 H25 A25 25 0 0 1 0 192 Z" fill="#bcbdc0"/>
      <path d="M0 20 A20 20 0 0 1 20 0 H252 A20 20 0 0 1 272 20 V108 H0 Z" fill="#ffffff"/>
      <path d="M14 100 H258 V185 A20 20 0 0 1 238 205 H34 A20 20 0 0 1 14 185 Z" fill="#ffffff"/>
    </svg>
    <div class="product-photo" role="img" aria-label="Photo of a satin chrome lever lockset"></div>
  </div>
  <div class="product-card" style="left:629px">
    <svg width="272" height="217" viewBox="0 0 272 217">
      <path d="M0 108 H272 V192 A25 25 0 0 1 247 217 H25 A25 25 0 0 1 0 192 Z" fill="#bcbdc0"/>
      <path d="M0 20 A20 20 0 0 1 20 0 H252 A20 20 0 0 1 272 20 V108 H0 Z" fill="#ffffff"/>
      <path d="M14 100 H258 V185 A20 20 0 0 1 238 205 H34 A20 20 0 0 1 14 185 Z" fill="#ffffff"/>
    </svg>
    <div class="product-photo" role="img" aria-label="Photo of two silver exit device push bars"></div>
  </div>

  <h2 class="join-title">JOIN US!</h2>
  <div class="pricing-banner">
    <svg width="386" height="40" viewBox="0 0 386 40">
      <polygon points="16,0 370,0 386,40 0,40" fill="#8a8b8e"/>
    </svg>
    <span class="pricing-text">FOR SPECIAL PRICING</span>
  </div>
  <p class="perks">Free Tacos, Prizes and more</p>

  <section class="brands-box">
    <span class="brands-label">Notable Brands We Carry</span>
    <div class="brand-corvanta">
      <span class="brand-square"></span>
      <span class="brand-name">CORVANTA</span>
    </div>
    <span class="brands-divider"></span>
    <span class="brand-marlow">MARLOW</span>
  </section>

  <div class="company-mark">
    <span class="mark-square"></span>
    <span class="company-name">
      <span class="line-1">TULVEN</span>
      <span class="line-2">COMMERCIAL DOOR</span>
    </span>
  </div>

  <svg class="contact-bands" width="944" height="1180" viewBox="0 0 944 1180">
    <polygon points="437,1106 460,1063 944,1063 944,1106" fill="#3b3c3e"/>
    <polygon points="415,1136 437,1106 944,1106 944,1136" fill="#d2d3d5"/>
    <circle cx="493" cy="1084" r="15" fill="#f0912c"/>
    <path d="M487 1077 l3 -1.5 3 5 -2 2 a9 9 0 0 0 4 4 l2 -2 5 3 -1.5 3 c-6 1 -14 -7 -13.5 -13.5 z" fill="#3b3c3e"/>
    <circle cx="486" cy="1121" r="10" fill="#141414"/>
    <circle cx="486" cy="1121" r="6.5" fill="none" stroke="#ffffff" stroke-width="1.3"/>
    <line x1="479.5" y1="1121" x2="492.5" y2="1121" stroke="#ffffff" stroke-width="1.2"/>
    <ellipse cx="486" cy="1121" rx="2.8" ry="6.5" fill="none" stroke="#ffffff" stroke-width="1.2"/>
  </svg>
  <p class="contact-phone">Call us <strong>555-014-2290</strong></p>
  <p class="contact-web">www.tulvencommercialdoor.com</p>
</main>
</body>
</html>
```